New Business Card for General Contractor Marketing

Need a business card the is more like a marketing promotion of our services
Must be horizontal orientation, One Sided Only, Max font size, Organize the Services
#1 General Contractor for Realtors
Remodels – Renovations – Repairs
Water & Mold Damage Experts
Painting: Interior/ Exterior
Flooring: Wood / LVT / Carpet
Plumbing: Repairs & Upgrades
Electric: Lights & Energy Efficient Upgrades
Kitchen & Bath Remodels
Fast Inspections Repair Billed Thru Escrow
BrightHarborBuilds.com
555-418-2796

Industry/Entity Type

General Contractor

Contact Information for Business Card

One Sided Only: #1 General Contractor for Realtors Remodels – Renovations – Repairs Water & Mold Damage Experts Painting: Interior/ Exterior Flooring: Wood / LVT / Carpet Plumbing: Repairs & Upgrades Electric: Lights & Energy Efficient Upgrades Kitchen & Bath Remodels Fast Inspections Repair Billed Thru Escrow BrightHarborBuilds.com 555-418-2796

Colors
0054AA
0677BA
7BADD7
CADEEF
E8F1F8

Requirements
Must have
• One Sided Only: #1 General Contractor for Realtors Remodels – Renovations – Repairs Water & Mold Damage Experts Painting: Interior/ Exterior Flooring: Wood / LVT / Carpet Plumbing: Repairs & Upgrades Electric: Lights & Energy Efficient Upgrades Kitchen & Bath Remodels Fast Inspections Repair Billed Thru Escrow BrightHarborBuilds.com 555-418-2796

```html
<!DOCTYPE html>
<html lang="en">
<head>
<meta charset="utf-8">
<title>Bright Harbor Builds – Business Card</title>
<link rel="stylesheet" href="https://fonts.googleapis.com/css2?family=Krona+One&family=Roboto+Condensed:wght@300&display=swap">
<style>
  :root {
    --navy: #1c2b5a;
    --orange: #f7800f;
    --white: #ffffff;
    --ink: #2a2a2a;
    --backdrop: #1b1b1b;
  }
  * { margin: 0; padding: 0; box-sizing: border-box; }
  html, body {
    width: 1200px;
    height: 1059px;
    overflow: hidden;
    background: var(--backdrop);
  }
  .card {
    position: absolute;
    left: 50px;
    top: 213px;
    width: 1100px;
    height: 633px;
    background: var(--white);
    border-radius: 39px;
    overflow: hidden;
    font-family: "Krona One", sans-serif;
  }
  .brand {
    position: absolute;
    left: 0;
    right: 0;
    top: 70px;
    display: flex;
    justify-content: center;
    align-items: center;
    gap: 18px;
  }
  .brand-mark {
    width: 40px;
    height: 40px;
    background: var(--orange);
  }
  .brand-name {
    font-size: 40px;
    color: var(--navy);
    letter-spacing: 0.5px;
    white-space: nowrap;
  }
  .headline {
    position: absolute;
    left: 0;
    right: 0;
    top: 245px;
    text-align: center;
    font-size: 36px;
    color: var(--navy);
    white-space: nowrap;
  }
  .tagline {
    position: absolute;
    left: 0;
    right: 0;
    top: 295px;
    text-align: center;
    font-size: 37px;
    color: var(--orange);
    white-space: nowrap;
  }
  .contact-band {
    position: absolute;
    left: 0;
    right: 0;
    top: 354px;
    height: 56px;
    background: var(--navy);
    display: flex;
    align-items: center;
    justify-content: center;
    gap: 40px;
    color: var(--white);
    font-size: 24px;
    padding-left: 60px;
  }
  .contact-item {
    display: flex;
    align-items: center;
    gap: 10px;
    white-space: nowrap;
  }
  .contact-item svg { display: block; }
  .services {
    position: absolute;
    top: 420px;
    left: 48px;
    right: 20px;
    display: grid;
    grid-template-columns: 473px 1fr;
    font-family: "Roboto Condensed", sans-serif;
    font-weight: 300;
    font-size: 31px;
    color: var(--ink);
    list-style: none;
  }
  .services ul { list-style: none; }
  .services li {
    height: 40px;
    line-height: 40px;
    white-space: nowrap;
  }
  .services li::before {
    content: "•";
    display: inline-block;
    width: 24px;
  }
  .rule {
    position: absolute;
    left: 0;
    right: 0;
    top: 557px;
    height: 6px;
    background: var(--orange);
  }
  .footer-band {
    position: absolute;
    left: 0;
    right: 0;
    top: 567px;
    bottom: 0;
    background: var(--navy);
    color: var(--white);
    font-size: 27px;
    display: flex;
    align-items: center;
    justify-content: center;
    white-space: nowrap;
  }
</style>
</head>
<body>
  <div class="card">
    <div class="brand">
      <span class="brand-mark"></span>
      <span class="brand-name">BRIGHT HARBOR BUILDS</span>
    </div>

    <h1 class="headline">#1 General Contractor for Realtors</h1>
    <p class="tagline">Remodels – Renovations – Repairs</p>

    <div class="contact-band">
      <span class="contact-item">
        <svg width="26" height="26" viewBox="0 0 24 24" aria-hidden="true">
          <path fill="#f7800f" d="M6.6 10.8a15.1 15.1 0 0 0 6.6 6.6l2.2-2.2a1 1 0 0 1 1-.25 11.4 11.4 0 0 0 3.6.57 1 1 0 0 1 1 1V20a1 1 0 0 1-1 1A17 17 0 0 1 3 4a1 1 0 0 1 1-1h3.5a1 1 0 0 1 1 1c0 1.25.2 2.45.57 3.57a1 1 0 0 1-.25 1z"/>
        </svg>
        555-418-2796
      </span>
      <span class="contact-item">
        <svg width="30" height="22" viewBox="0 0 30 22" aria-hidden="true">
          <rect x="1" y="2" width="28" height="19" fill="#f7800f"/>
          <path d="M2 3 L15 13 L28 3" fill="none" stroke="#1c2b5a" stroke-width="2.5"/>
        </svg>
        BrightHarborBuilds.com
      </span>
    </div>

    <div class="services">
      <ul>
        <li>Water &amp; Mold Damage Experts</li>
        <li>Painting: Interior/ Exterior</li>
        <li>Flooring: Wood / LVT / Carpet</li>
      </ul>
      <ul>
        <li>Plumbing: Repairs &amp; Upgrades</li>
        <li>Electric: Lights &amp; Energy Efficient Upgrades</li>
        <li>Kitchen &amp; Bath Remodels</li>
      </ul>
    </div>

    <div class="rule"></div>
    <div class="footer-band">Fast Inspections Repair Billed Thru Escrow</div>
  </div>
</body>
</html>
```